Need to design a business card with logo

Hellow
we are a company ,
PT KORAN MELATI JAYA
looking for design of name card.
what we do is property development and management.
design preferable professional corporate look and feel.
corporate. color, pantone colour 289
information required is
company name " Koran Melati Jaya"
person name eg " Peter Walsh"
person title eg "secret agent"
address: 12 heron lane , jakarta, indonesia
phone : +6221 5917264
mobile : 0812 463 518
email : peter@walshmail.example
website: www.peterwa.example
if you want to include logo in the design you are welcome and appreciated , or you can simply use the company name as the logo.
thanks
Target Market(s)
corporate , business person , show events, exhibition events ,etc
Industry/Entity Type
Business
Look and feel
Each slider illustrates characteristics of the customer's brand and the style your logo design should communicate.

```html
<!DOCTYPE html>
<html lang="en">
<head>
<meta charset="utf-8">
<title>Koran Melati Jaya — Business Card</title>
<link rel="stylesheet" href="https://fonts.googleapis.com/css2?family=Open+Sans:ital,wght@0,400;0,600;0,700;1,700&display=swap">
<style>
  :root {
    --navy: #29295c;
    --navy-line: #6d6d99;
    --ink: #2b2b2b;
    --paper: #ffffff;
    --backdrop: #e6e7ea;
  }
  * { box-sizing: border-box; margin: 0; padding: 0; }
  html, body {
    width: 1200px; height: 926px; overflow: hidden;
    background: var(--backdrop);
    font-family: "Open Sans", Arial, sans-serif;
  }
  .card {
    position: absolute; left: 260px;
    width: 680px; height: 390px;
    overflow: hidden;
    box-shadow: 0 6px 18px rgba(0,0,0,.18);
  }

  /* Front */
  .card-front { top: 50px; background: var(--paper); }
  .band { position: absolute; left: 0; right: 0; background: var(--navy); }
  .band-top { top: 0; height: 26px; }
  .band-bottom { bottom: 0; height: 50px; }
  .rule { position: absolute; left: 0; right: 0; height: 1px; background: var(--navy-line); }
  .rule-top { top: 36px; }
  .rule-bottom { bottom: 60px; }
  .company-vertical {
    position: absolute; left: 58px; top: 62px;
    transform-origin: left top;
    transform: rotate(-90deg) translateX(-100%);
    color: var(--navy); font-weight: 700; font-size: 21px;
    white-space: nowrap;
  }
  .identity { position: absolute; right: 40px; top: 78px; text-align: right; }
  .person-name { font-size: 36px; color: var(--ink); line-height: 1; letter-spacing: -.5px; }
  .person-name .first { font-weight: 700; }
  .person-name .last { font-weight: 400; }
  .company-name { font-size: 15px; color: var(--navy); margin-top: 2px; }
  .contact {
    position: absolute; right: 40px; top: 170px;
    display: grid; grid-template-columns: auto 96px;
    row-gap: 3px; column-gap: 18px;
    font-size: 15px; line-height: 22px;
  }
  .contact .value { text-align: right; color: var(--ink); }
  .contact .label { color: var(--navy); font-weight: 600; }
  .contact .label::before { content: "| "; font-weight: 400; }

  /* Back */
  .card-back { top: 480px; background: var(--navy); }
  .back-rule { position: absolute; left: 0; right: 0; top: 230px; height: 1px; background: var(--navy-line); }
  .back-strip {
    position: absolute; left: 34px; right: 34px; top: 248px; height: 96px;
    background: var(--paper);
  }
  .back-phone {
    position: absolute; left: 14px; top: 10px;
    font-size: 18px; font-weight: 700; font-style: italic; color: var(--navy);
  }
  .back-company {
    position: absolute; right: 16px; bottom: 12px;
    font-size: 21px; font-weight: 700; color: var(--navy);
  }
</style>
</head>
<body>
  <section class="card card-front" aria-label="Business card front">
    <div class="band band-top"></div>
    <div class="rule rule-top"></div>
    <div class="company-vertical">Koran Melati Jaya</div>
    <div class="identity">
      <h1 class="person-name"><span class="first">Peter</span> <span class="last">Walsh</span></h1>
      <p class="company-name">Koran Melati Jaya</p>
    </div>
    <dl class="contact">
      <dd class="value">12 heron lane , jakarta, indonesia</dd><dt class="label">address</dt>
      <dd class="value">+6221 5917264</dd><dt class="label">phone</dt>
      <dd class="value">0812 463 518</dd><dt class="label">mobile</dt>
      <dd class="value">peter@walshmail.example</dd><dt class="label">email</dt>
      <dd class="value">www.peterwa.example</dd><dt class="label">website</dt>
    </dl>
    <div class="rule rule-bottom"></div>
    <div class="band band-bottom"></div>
  </section>

  <section class="card card-back" aria-label="Business card back">
    <div class="back-rule"></div>
    <div class="back-strip">
      <p class="back-phone">+6221 5917264</p>
      <p class="back-company">Koran Melati Jaya</p>
    </div>
  </section>
</body>
</html>
```